Progressive Flow Chart

Looking for a progressive flow chart centered and branching off. They all build on each other 1-3. There will be 3 different pages.

Target Market(s)

Business Owners - High Net worth Individuals

Industry/Entity Type

Finance & Business Consulting

Font styles to use
Serif

Colors
0054AA
0677BA
7BADD7
CADEEF
E8F1F8
0094D4
00A9DD
6FCCEA
C7EBF8
E9F6FB
00AB8E
00BBA5
67D7C9
C6EFE9
E9F9F6

Requirements
Nice to have
• Clean, simple, and approachable.
Should not have
• Very Busy

```html
<!DOCTYPE html>
<html lang="en">
<head>
<meta charset="utf-8">
<title>Living Trust Flow Chart</title>
<link href="https://fonts.googleapis.com/css2?family=Montserrat:wght@400;500;700;800&display=swap" rel="stylesheet">
<style>
  :root {
    --navy: #0f1a3d;
    --blue-deep: #0094D4;
    --blue: #00A9DD;
    --blue-soft: #6FCCEA;
    --blue-pale: #E9F6FB;
    --teal: #00BBA5;
    --teal-soft: #67D7C9;
    --core: #8AC8EE;
    --white: #ffffff;
  }
  html, body {
    margin: 0;
    padding: 0;
    width: 1200px;
    height: 848px;
    overflow: hidden;
    background: var(--white);
  }
  .flow-chart {
    display: block;
    width: 1200px;
    height: 848px;
    font-family: "Montserrat", sans-serif;
  }
  .node-box { fill: url(#boxFill); stroke: url(#edgeStroke); stroke-width: 3; }
  .node-title { fill: var(--navy); font-weight: 800; }
  .node-title--xl { font-size: 66px; letter-spacing: 1px; }
  .node-title--md { font-size: 34px; }
  .node-title--sm { font-size: 30px; }
  .node-detail { fill: var(--navy); font-size: 17px; font-weight: 500; }
  .flow-line { fill: none; stroke: var(--blue); stroke-width: 3; }
  .flow-line--teal { stroke: var(--teal-soft); }
  .flow-label { fill: var(--navy); font-size: 19px; font-weight: 500; letter-spacing: 0.5px; }
  .trust-label { fill: var(--white); font-size: 24px; font-weight: 500; letter-spacing: 1px; }
  .you-label { fill: #000; font-size: 96px; font-weight: 800; }
  .trustee-label { fill: var(--navy); font-size: 18px; font-weight: 700; letter-spacing: 4px; }
  .icon-fill { fill: url(#iconFill); }
  .icon-line { fill: none; stroke: url(#iconFill); stroke-width: 3; }
  .brand-name { fill: var(--blue-soft); font-size: 22px; font-weight: 700; letter-spacing: 2px; }
  .brand-dot { fill: var(--blue-soft); }
</style>
</head>
<body>
<svg class="flow-chart" viewBox="0 0 1500 1060" xmlns="http://www.w3.org/2000/svg" aria-label="Living trust planning flow chart">
  <defs>
    <linearGradient id="boxFill" x1="0" y1="0" x2="1" y2="1">
      <stop offset="0" stop-color="#eef7fc"/>
      <stop offset="1" stop-color="#e2f2f8"/>
    </linearGradient>
    <linearGradient id="edgeStroke" x1="0" y1="0" x2="1" y2="1">
      <stop offset="0" stop-color="#00A9DD"/>
      <stop offset="1" stop-color="#67D7C9"/>
    </linearGradient>
    <linearGradient id="iconFill" x1="0" y1="0" x2="1" y2="1">
      <stop offset="0" stop-color="#0094D4"/>
      <stop offset="1" stop-color="#67D7C9"/>
    </linearGradient>
    <linearGradient id="trustFill" x1="0" y1="0" x2="0.3" y2="1">
      <stop offset="0" stop-color="#3fb0d3"/>
      <stop offset="1" stop-color="#63c2ad"/>
    </linearGradient>
    <marker id="arrowBlue" viewBox="0 0 10 10" refX="8" refY="5" markerWidth="6" markerHeight="6" orient="auto-start-reverse">
      <path d="M0 0 L10 5 L0 10 z" fill="#00A9DD"/>
    </marker>
    <marker id="arrowTeal" viewBox="0 0 10 10" refX="8" refY="5" markerWidth="6" markerHeight="6" orient="auto-start-reverse">
      <path d="M0 0 L10 5 L0 10 z" fill="#4fc3b8"/>
    </marker>
  </defs>

  <!-- Top strategy tiles -->
  <g class="tile tile--crt">
    <rect class="node-box" x="97" y="84" width="333" height="156" rx="26"/>
    <g class="icon-line">
      <rect x="138" y="127" width="72" height="72" rx="4"/>
      <rect x="152" y="127" width="40" height="18"/>
      <line x1="138" y1="185" x2="210" y2="185"/>
    </g>
    <text x="152" y="178" font-size="16" font-weight="800" fill="#0094D4">CRT</text>
    <text class="node-title node-title--xl" x="252" y="187">CRT</text>
  </g>

  <g class="tile tile--daf">
    <rect class="node-box" x="598" y="84" width="333" height="156" rx="26"/>
    <path class="icon-fill" d="M650 130 h36 l14 14 v50 h-50 z"/>
    <g fill="#fff">
      <rect x="657" y="146" width="16" height="4"/><rect x="657" y="156" width="16" height="4"/><rect x="657" y="166" width="16" height="4"/>
    </g>
    <text x="662" y="191" font-size="12" font-weight="700" fill="#fff">DAF</text>
    <text class="node-title node-title--xl" x="732" y="187">DAF</text>
  </g>

  <g class="tile tile--grats">
    <rect class="node-box" x="1070" y="84" width="333" height="156" rx="26"/>
    <path class="icon-fill" d="M1144 122 l10 30 h32 l-26 19 l10 30 l-26 -18 l-26 18 l10 -30 l-26 -19 h32 z"/>
    <text class="node-title node-title--md" x="1210" y="150">GRATS</text>
    <text class="node-title node-title--md" x="1210" y="196">IDGTS</text>
  </g>

  <!-- Brand -->
  <g class="brand" aria-label="Northvale Financial">
    <circle class="brand-dot" cx="1248" cy="440" r="14"/>
    <text class="brand-name" x="1248" y="500" text-anchor="middle">NORTHVALE FINANCIAL</text>
  </g>

  <!-- Connecting lines -->
  <g class="flows">
    <line class="flow-line" x1="527" y1="489" x2="446" y2="489" marker-end="url(#arrowBlue)"/>
    <text class="flow-label" x="446" y="533">INVEST</text>

    <line class="flow-line" x1="202" y1="808" x2="202" y2="582" marker-end="url(#arrowBlue)"/>
    <text class="flow-label" transform="translate(186 740) rotate(-90)">INTEREST</text>

    <line class="flow-line" x1="263" y1="582" x2="263" y2="758" marker-end="url(#arrowBlue)"/>
    <line class="flow-line" x1="263" y1="758" x2="263" y2="808"/>
    <text class="flow-label" transform="translate(254 720) rotate(-90)">INVESTMENT</text>

    <line class="flow-line" x1="263" y1="808" x2="404" y2="721" marker-end="url(#arrowBlue)"/>
    <line class="flow-line flow-line--teal" x1="404" y1="721" x2="546" y2="633" marker-end="url(#arrowTeal)"/>
    <text class="flow-label" transform="translate(304 774) rotate(-31)">INCOME</text>

    <line class="flow-line" x1="263" y1="582" x2="566" y2="726" marker-end="url(#arrowBlue)"/>
    <line class="flow-line flow-line--teal" x1="566" y1="726" x2="733" y2="805" marker-end="url(#arrowTeal)"/>

    <line class="flow-line flow-line--teal" x1="603" y1="897" x2="443" y2="897" marker-end="url(#arrowBlue)"/>
    <text class="flow-label" x="500" y="886">RENT</text>

    <line class="flow-line" x1="770" y1="818" x2="770" y2="772" marker-end="url(#arrowBlue)"/>
    <text class="flow-label" x="805" y="801">INCOME</text>

    <line class="flow-line" x1="1015" y1="518" x2="1307" y2="818"/>
    <line class="flow-line flow-line--teal" x1="1003" y1="597" x2="1230" y2="818"/>
  </g>

  <!-- Centre trust -->
  <g class="trust">
    <circle cx="777" cy="521" r="240" fill="url(#trustFill)"/>
    <circle cx="777" cy="521" r="140" fill="var(--core)" stroke="#fff" stroke-width="4"/>
    <text class="trust-label" x="777" y="345" text-anchor="middle">LIVING TRUST</text>
    <text class="you-label" x="775" y="538" text-anchor="middle">YOU</text>
    <text class="trustee-label" x="777" y="567" text-anchor="middle">TRUSTEE</text>
  </g>

  <!-- Bank -->
  <g class="tile tile--bank">
    <rect class="node-box" x="97" y="411" width="333" height="157" rx="26"/>
    <g class="icon-fill">
      <path d="M131 478 l33 -20 l33 20 z"/>
      <rect x="137" y="483" width="6" height="22"/><rect x="150" y="483" width="6" height="22"/>
      <rect x="163" y="483" width="6" height="22"/><rect x="176" y="483" width="6" height="22"/>
      <rect x="188" y="483" width="6" height="22"/>
      <rect x="131" y="508" width="66" height="5"/><rect x="133" y="516" width="62" height="4"/>
    </g>
    <text class="node-title node-title--sm" x="213" y="468">BANK</text>
    <text class="node-detail" x="214" y="493">MAKES INVESTMENTS</text>
    <text class="node-detail" x="214" y="514">IN REAL ESTATE +</text>
    <text class="node-detail" x="214" y="535">BUSINESS</text>
  </g>

  <!-- Real estate -->
  <g class="tile tile--real-estate">
    <rect class="node-box" x="97" y="820" width="333" height="156" rx="26"/>
    <g class="icon-fill">
      <rect x="142" y="864" width="26" height="62"/>
      <rect x="158" y="890" width="14" height="36"/>
      <rect x="176" y="876" width="22" height="50"/>
      <rect x="136" y="927" width="68" height="3"/>
    </g>
    <g fill="#fff">
      <rect x="147" y="870" width="5" height="5"/><rect x="157" y="870" width="5" height="5"/>
      <rect x="147" y="881" width="5" height="5"/><rect x="157" y="881" width="5" height="5"/>
      <rect x="147" y="892" width="5" height="5"/>
    </g>
    <text class="node-title node-title--sm" x="231" y="870">REAL</text>
    <text class="node-title node-title--sm" x="231" y="908">ESTATE</text>
    <text class="node-title node-title--sm" x="231" y="946">LLC</text>
  </g>

  <!-- Business -->
  <g class="tile tile--business">
    <rect class="node-box" x="605" y="820" width="333" height="156" rx="26"/>
    <rect class="icon-fill" x="641" y="870" width="60" height="42" rx="5"/>
    <rect x="647" y="876" width="48" height="28" fill="#e9f6fb"/>
    <rect class="icon-fill" x="660" y="914" width="22" height="8"/>
    <circle cx="658" cy="890" r="5" fill="#0094D4"/>
    <circle cx="685" cy="890" r="6" fill="#00BBA5"/>
    <text class="node-title" font-size="24" x="735" y="874">BUSINESS</text>
    <text class="node-detail" font-weight="400" x="735" y="898">LLC - MEMBER</text>
    <text class="node-detail" font-weight="400" x="735" y="921">MANAGER CORP</text>
    <text class="node-detail" font-weight="400" x="735" y="944">PRESIDENT</text>
  </g>

  <!-- Insurance -->
  <g class="tile tile--insurance">
    <rect class="node-box" x="1067" y="820" width="333" height="156" rx="26"/>
    <path class="icon-fill" d="M1108 893 a26 26 0 0 1 52 0 z"/>
    <rect class="icon-fill" x="1132" y="862" width="4" height="36"/>
    <path class="icon-fill" d="M1096 922 l14 -14 h22 c8 0 8 8 0 8 h-10 l24 -6 c6 -2 10 4 4 8 l-26 14 h-18 l-6 6 z"/>
    <text class="node-title node-title--sm" x="1181" y="910">INSURANCE</text>
  </g>
</svg>
</body>
</html>
```